General Contractor/ Real Estate Family Business AMAZING Drywall/Paint Flyer

We need to have a flyer designed to market our drywall repair services. We are looking to increase our business in this field and plan on using this flyer in both print and as an eflyer to use in email marketing campaigns. We would like to incorporate past flyer designs and colors/ logos into this flyer so our marketing stays consistent.

Target Market(s)

Drywall repair, Insurance Restoration, Real Estate Agents, Property Managers, Real Estate Investors, Single family residential homeowners.

Industry/Entity Type

Real Estate

Font styles to use
Sans Serif

Requirements
Must have
• Must include the logos provided, pictures provided, and incorporate the copy provided in the attached word document. Must include our license number. Must be able to fit a standard 8.5"x11" flyer size. Must also be optimized to use online as an eflyer in online marketing campaigns.
Nice to have
• It would be nice to incorporate some of the designs and colors form previous flyers to keep our marketing consistent. Past flyers are attached in the documents.

```html
<!DOCTYPE html>
<html lang="en">
<head>
<meta charset="utf-8">
<title>Corvano Property Solutions – Drywall & Painting Flyer</title>
<link href="https://fonts.googleapis.com/css2?family=Barlow+Semi+Condensed:wght@400;500;600;700&display=swap" rel="stylesheet">
<style>
  :root {
    --backdrop: #b3b3b3;
    --paper: #ffffff;
    --ink: #1a1a1a;
    --brand-blue: #1d4aa6;
    --cta-blue: #1f9de2;
    --footer-black: #0b0b0b;
    --panel-dark: rgba(38, 42, 48, 0.88);
    --muted: #333333;
  }
  * { margin: 0; padding: 0; box-sizing: border-box; }
  html, body {
    width: 1200px; height: 1020px; overflow: hidden;
    background: var(--backdrop);
    font-family: "Barlow Semi Condensed", "Arial Narrow", sans-serif;
    color: var(--ink);
  }
  .flyer {
    position: absolute; left: 320px; top: 115px;
    width: 560px; height: 791px;
    background: var(--paper);
    overflow: hidden;
  }
  .masthead { position: absolute; left: 0; top: 0; width: 560px; height: 144px; }
  .brand {
    position: absolute; left: 26px; top: 48px;
    display: flex; align-items: center; gap: 10px;
    font-weight: 600; font-size: 22px; color: var(--brand-blue);
    line-height: 1.05;
  }
  .brand-dot { width: 18px; height: 18px; border-radius: 50%; background: var(--brand-blue); flex: none; }
  .contact { position: absolute; left: 358px; top: 69px; }
  .license { font-weight: 700; font-size: 16px; color: var(--brand-blue); margin-bottom: 5px; }
  .contact-row { display: flex; font-size: 9.5px; line-height: 12px; color: var(--ink); }
  .contact-row dt { width: 41px; font-weight: 700; }
  .hero { position: absolute; left: 0; top: 144px; width: 560px; height: 338px; }
  .hero-photo {
    position: absolute; inset: 0;
    background: linear-gradient(180deg, #2f6fd0 0%, #6fa0dc 35%, #7d5a3e 55%, #b07e58 75%, #c9a27f 100%);
  }
  .hero-panel {
    position: absolute; left: 270px; top: 0; width: 290px; height: 338px;
    background: var(--panel-dark);
  }
  .hero-title {
    position: absolute; left: 44px; top: 26px;
    font-weight: 600; font-size: 32px; line-height: 40.5px; color: #ffffff;
  }
  .section { position: absolute; top: 500px; }
  .services { left: 24px; width: 230px; }
  .about { left: 271px; width: 270px; }
  .section-title {
    display: flex; align-items: center; gap: 16px;
    font-weight: 700; font-size: 18px; letter-spacing: 0.2px; height: 22px;
  }
  .section-title::before {
    content: ""; width: 3px; height: 15px; background: var(--brand-blue);
  }
  .bullets { list-style: none; margin-top: 13px; }
  .bullets li {
    position: relative; padding-left: 22px;
    font-size: 10px; line-height: 12.6px; color: var(--muted);
  }
  .bullets li::before {
    content: ""; position: absolute; left: 0; top: 2px;
    width: 7px; height: 7px; border: 1.5px solid var(--brand-blue); border-radius: 50%;
  }
  .services .bullets li { margin-bottom: 14.4px; }
  .about .bullets li { line-height: 13.2px; margin-bottom: 10.8px; }
  .cta-band {
    position: absolute; left: 0; top: 725px; width: 560px; height: 66px;
    background: var(--footer-black); text-align: center; color: #ffffff;
  }
  .cta-title { margin-top: 12px; font-weight: 700; font-size: 17px; color: var(--cta-blue); }
  .cta-text { font-size: 10.5px; margin-top: 1px; }
</style>
</head>
<body>
  <main class="flyer">
    <header class="masthead">
      <div class="brand"><span class="brand-dot"></span><span>Corvano<br>Property Solutions, LLC</span></div>
      <div class="contact">
        <p class="license">ROC #318205</p>
        <dl>
          <div class="contact-row"><dt>Phone:</dt><dd>(602) 555-0147</dd></div>
          <div class="contact-row"><dt>Email:</dt><dd>solutions@corvanoproperties.com</dd></div>
          <div class="contact-row"><dt>Website:</dt><dd>www.corvanopropertysolutions.com</dd></div>
        </dl>
      </div>
    </header>

    <section class="hero">
      <div class="hero-photo" role="img" aria-label="Photo of a tiled-roof home with a paved patio and backyard pool under a blue sky"></div>
      <div class="hero-panel">
        <h1 class="hero-title">Top Quality<br>Drywall Repair,<br>Installation,<br>Painting &amp;<br>Insurance<br>Restoration<br>Services!</h1>
      </div>
    </section>

    <section class="section services">
      <h2 class="section-title">SERVICES</h2>
      <ul class="bullets">
        <li>Drywall Repair and Hole Patching</li>
        <li>New Drywall Installation and Hanging</li>
        <li>Popcorn Ceiling Removal</li>
        <li>All Textures- Orange Peel, Knockdown,</li>
        <li>Smooth Finish, Skip Trowel</li>
        <li>Complete Interior and Exterior Painting</li>
        <li>Insurance Restoration- Fire, Water Damage</li>
      </ul>
    </section>

    <section class="section about">
      <h2 class="section-title">ABOUT US</h2>
      <ul class="bullets">
        <li>Corvano Property Solutions LLC has 10+ years' experience here in Maricopa County.</li>
        <li>Locally owned family business with an A+ HRC rating, full general contractor license/insurance.</li>
        <li>We can handle your entire drywall, painting, or restoration project- no need to hire multiple companies or subs. Just bring us in and let us give you a stress free one stop shop<br>experience.</li>
        <li>Customers who work with us typically hire us for our professional quality work that's always consistent, reliable, and completed on deadline.</li>
      </ul>
    </section>

    <footer class="cta-band">
      <p class="cta-title">Call To Action To Incorporate :</p>
      <p class="cta-text">Contact us today to discuss your project and receive a free estimate within 72 hours!</p>
    </footer>
  </main>
</body>
</html>
```